Postcard Design

Need a post card looking to attract brides and interns at a trade show. love to use my logo and an image or two of past events and maybe a background pic fading behind the verbage. pick whatever images you think work.
Gilded Galas
couture coordination for fashionable events
Marla Quintrell, MBC
marla@gilded-galas.com

```html
<!DOCTYPE html>
<html lang="en">
<head>
<meta charset="utf-8">
<title>Gilded Galas Postcard</title>
<link rel="stylesheet" href="https://fonts.googleapis.com/css2?family=Oswald:wght@400;500;700&family=Open+Sans:wght@400;600;700&display=swap">
<style>
  :root {
    --gold: #e9a21f;
    --gold-deep: #c9820f;
    --charcoal: #2e2e30;
    --grey: #5a5a5c;
    --light: #f4f2ee;
    --white: #ffffff;
    --stage: #e6e3de;
  }
  * { margin: 0; padding: 0; box-sizing: border-box; }
  html, body { width: 887px; height: 1200px; overflow: hidden; background: var(--stage); }
  body { position: relative; font-family: "Open Sans", sans-serif; color: var(--grey); }
  .postcard { position: absolute; left: 43px; width: 800px; height: 550px; background: var(--white); overflow: hidden; box-shadow: 0 6px 18px rgba(0,0,0,.25); }
  .front { top: 40px; }
  .back { top: 620px; }
  .abs { position: absolute; }
  .shapes { position: absolute; inset: 0; }

  /* Front */
  .couple-photo { left: 0; top: 0; width: 560px; height: 550px; background: linear-gradient(135deg, #7c9a5a 0%, #b8c79a 40%, #efece4 60%, #a7ae93 100%); }
  .logo { left: 540px; top: 28px; width: 240px; text-align: center; }
  .logo-name { font-family: "Oswald", sans-serif; font-weight: 500; font-size: 38px; color: var(--grey); letter-spacing: 1px; }
  .logo-sub { font-size: 12px; color: var(--gold-deep); letter-spacing: 1px; }
  .tagline { left: 540px; top: 140px; width: 240px; text-align: center; font-family: "Oswald", sans-serif; line-height: 1.1; }
  .tagline .t1 { font-size: 23px; color: var(--grey); letter-spacing: 1px; }
  .tagline .t2 { font-size: 30px; color: var(--gold); letter-spacing: 1px; }
  .tagline .t3 { font-size: 70px; color: var(--grey); font-weight: 400; letter-spacing: 2px; }
  .date-badge { left: 392px; top: 258px; width: 150px; height: 150px; text-align: center; font-family: "Oswald", sans-serif; padding-top: 34px; }
  .date-badge .day { font-size: 44px; color: var(--gold); font-weight: 700; line-height: 1; }
  .date-badge .day sup { font-size: 20px; }
  .date-badge .month { font-size: 15px; color: var(--white); letter-spacing: 2px; }
  .weekday { left: 560px; top: 300px; width: 240px; height: 60px; font-family: "Oswald", sans-serif; font-size: 44px; font-weight: 700; color: var(--white); text-align: center; line-height: 60px; letter-spacing: 2px; }
  .signature { left: 560px; top: 484px; width: 230px; color: var(--white); }
  .signature .name { font-size: 17px; font-weight: 600; }
  .signature .email { font-size: 11px; color: var(--gold); }

  /* Back */
  .faded-venue { left: 0; top: 0; width: 420px; height: 550px; background: linear-gradient(180deg, #ffffff 0%, #f1ece2 45%, #e3d6bf 100%); opacity: .9; }
  .headline { left: 26px; top: 24px; font-family: "Oswald", sans-serif; line-height: 1.15; }
  .headline .h1 { font-size: 24px; color: var(--grey); }
  .headline .h2 { font-size: 28px; color: var(--gold); }
  .value-band { left: 0; top: 108px; width: 230px; height: 36px; background: var(--gold); color: var(--white); font-family: "Oswald", sans-serif; font-size: 22px; font-weight: 700; padding-left: 26px; line-height: 36px; }
  .values { left: 26px; top: 152px; font-size: 13px; color: var(--gold-deep); font-weight: 600; }
  .intro { left: 26px; top: 190px; width: 320px; font-size: 13px; line-height: 1.45; color: var(--grey); }
  .event-photo { width: 110px; height: 110px; border-radius: 50%; border: 5px solid var(--white); box-shadow: 0 0 0 2px var(--gold); }
  .bouquet { left: 36px; top: 300px; background: radial-gradient(circle, #f2a24a 0%, #c9611c 60%, #6e3a16 100%); }
  .portrait { left: 166px; top: 300px; background: radial-gradient(circle, #8a6b4a 0%, #3b2a1d 70%); }
  .contact-band { left: 0; top: 448px; width: 410px; height: 102px; background: var(--gold); }
  .contact-note { left: 26px; top: 460px; width: 170px; color: var(--white); font-size: 17px; line-height: 1.25; }
  .contact-note strong { color: var(--charcoal); font-weight: 700; }
  .contact-card { left: 200px; top: 460px; width: 190px; height: 78px; background: var(--white); padding: 6px 10px; }
  .contact-card .name { font-size: 12px; color: var(--grey); font-weight: 600; }
  .contact-card .phone { font-family: "Oswald", sans-serif; font-size: 26px; color: var(--gold-deep); line-height: 1.15; }
  .contact-card .email { font-size: 11px; color: var(--grey); }
  .stamp-box { left: 690px; top: 30px; width: 80px; height: 96px; border: 2px solid #b9b9b9; }
</style>
</head>
<body>

<section class="postcard front">
  <div class="abs couple-photo" role="img" aria-label="Photo of a bride and groom embracing outdoors on their wedding day"></div>
  <svg class="shapes" viewBox="0 0 800 550" aria-hidden="true">
    <path d="M500,0 C455,170 470,390 545,550 L800,550 L800,0 Z" fill="var(--white)"/>
    <path d="M500,0 C455,170 470,390 545,550" fill="none" stroke="var(--gold)" stroke-width="8"/>
    <path d="M520,0 C480,170 492,390 565,550" fill="none" stroke="var(--charcoal)" stroke-width="4"/>
    <path d="M610,0 C660,30 740,40 800,20 L800,0 Z" fill="var(--gold)"/>
    <path d="M548,468 L800,468 L800,550 L560,550 C552,525 549,496 548,468 Z" fill="var(--charcoal)"/>
    <path d="M548,462 L800,462" stroke="var(--gold)" stroke-width="4"/>
    <polygon points="560,300 800,300 800,360 560,360 575,330" fill="var(--gold)"/>
    <polygon points="560,360 800,360 800,366 560,366" fill="var(--gold-deep)"/>
    <circle cx="467" cy="333" r="76" fill="var(--charcoal)"/>
    <circle cx="467" cy="333" r="66" fill="none" stroke="var(--gold)" stroke-width="3"/>
  </svg>
  <div class="abs logo">
    <div class="logo-name">Gilded Galas</div>
    <div class="logo-sub">weddings &amp; fashionable events</div>
  </div>
  <div class="abs tagline">
    <div class="t1">COUTURE COORDINATION</div>
    <div class="t2">FOR FASHIONABLE</div>
    <div class="t3">EVENTS</div>
  </div>
  <div class="abs date-badge">
    <div class="day">30<sup>th</sup></div>
    <div class="month">SEPTEMBER</div>
  </div>
  <div class="abs weekday">TUESDAY</div>
  <div class="abs signature">
    <div class="name">Marla Quintrell, MBC</div>
    <div class="email">marla@gilded-galas.com</div>
  </div>
</section>

<section class="postcard back">
  <div class="abs faded-venue" role="img" aria-label="Faded background photo of a decorated wedding reception venue"></div>
  <svg class="shapes" viewBox="0 0 800 550" aria-hidden="true">
    <path d="M360,0 L430,0 C395,150 400,330 430,550 L410,550 C380,330 380,150 360,0 Z" fill="var(--charcoal)"/>
    <path d="M345,0 C372,150 372,330 400,550" fill="none" stroke="var(--gold)" stroke-width="6"/>
  </svg>
  <div class="abs headline">
    <div class="h1">THE BEST WEDDING PLANNER</div>
    <div class="h2">IN CINCINNATI PERIOD</div>
  </div>
  <div class="abs value-band">ELEGANCE:</div>
  <div class="abs values">Style, Grace, Sumptuousness, Chic</div>
  <p class="abs intro">Specializing in wedding day coordination for the fashionable bride and unsurpassed in expertise and passion. This day, of all days, you deserve the best.</p>
  <div class="abs event-photo bouquet" role="img" aria-label="Photo of an orange wedding bouquet"></div>
  <div class="abs event-photo portrait" role="img" aria-label="Photo of a bride at a past event"></div>
  <div class="abs contact-band"></div>
  <div class="abs contact-note">Please <strong>contact us</strong> for date availability and rate information.</div>
  <div class="abs contact-card">
    <div class="name">Marla Quintrell, MBC</div>
    <div class="phone">555-014-2288</div>
    <div class="email">marla@gilded-galas.com</div>
  </div>
  <div class="abs stamp-box"></div>
</section>

</body>
</html>
```